I need a very simple poster with the following quote:
"Cada escolha, uma renĂșncia, isso Ă© a vida"
Which means that to every choice there is a waiver, that's life.

It will be framed and used in my living room.

The poster has to be black and white. It is not mandatory to use commas and quotes.

The design has to be modern, like the references I posted on this board: http://pinboardly.example/marvetu/ideas/

```html
<!DOCTYPE html>
<html lang="pt">
<head>
<meta charset="utf-8">
<title>Cada escolha, uma renúncia — poster</title>
<link rel="stylesheet" href="https://fonts.googleapis.com/css2?family=Cinzel:wght@700&display=swap">
<style>
  :root {
    --ink: #0b0b0b;
    --surface-dark: #8f8f8f;
    --surface-mid: #b9b9b9;
    --paper: #f4f2ec;
    --paper-shade: #e4e1d9;
  }
  html, body {
    margin: 0;
    padding: 0;
    width: 1200px;
    height: 796px;
    overflow: hidden;
    background: var(--surface-mid);
  }
  .poster {
    position: relative;
    width: 1200px;
    height: 796px;
    overflow: hidden;
  }
  .poster__photo {
    position: absolute;
    inset: 0;
    background:
      linear-gradient(160deg, transparent 0 8%, var(--paper) 30%, var(--paper-shade) 70%, var(--surface-mid) 96%),
      linear-gradient(90deg, var(--surface-dark), var(--surface-mid));
  }
  .poster__quote {
    position: absolute;
    left: 690px;
    top: 345px;
    margin: 0;
    transform: translate(-50%, -50%) rotate(15deg);
    font-family: "Cinzel", "Times New Roman", serif;
    font-weight: 700;
    font-size: 62px;
    line-height: 74px;
    color: var(--ink);
    text-align: center;
    letter-spacing: 0.01em;
    white-space: nowrap;
  }
  .poster__line { display: block; }
</style>
</head>
<body>
  <main class="poster">
    <div class="poster__photo" role="img" aria-label="Photograph of cream envelopes on a grey surface, closed with a black wax seal, with a wooden seal stamp resting on top"></div>
    <h1 class="poster__quote">
      <span class="poster__line">Cada</span>
      <span class="poster__line">escolha,</span>
      <span class="poster__line">uma</span>
      <span class="poster__line">renúncia,</span>
      <span class="poster__line">isso é a vida</span>
    </h1>
  </main>
</body>
</html>
```